Meridale Tax Advisers Business Card

We are seeking a clean, professional, and modern double sided business card design for Meridale Tax Advisers, a tax, accounting, and advisory firm serving business owners, professionals, and investors.
The design should convey credibility, precision, trust, and sophistication appropriate for a CPA level tax advisory firm. Avoid playful, trendy, or overly decorative styles. The look should be sharp, balanced, and timeless.
Our official company logo has been uploaded, which must be incorporated appropriately and consistently with the brand. Designers should not modify, distort, or recreate the logo.
Card format
Standard US business card size (3.5 x 2 inches)
Double sided
Design direction
Professional and modern
Minimalist and uncluttered
Strong typography and clean spacing
Subtle visual interest is welcome, but simplicity is preferred
High contrast and readability are critical
Front side
Primary focus on the Meridale Tax Advisers logo
The firm name should be clearly legible and visually prominent
Background may be white or dark, depending on what best complements the logo
Back side
Contact information layout, such as
Name: Peter L. Garnick, MSA, CFP®, AIF®, EA
Title: Managing Director, Tax
Email: pgarnick@mymeridale.example
Website: https://www.meridale.example/
Mobile: (555) 318-2047
Direct: (555) 642-7130
Main: (555) 642-7188
Address: 2870 Fenwick Rd., Suite 415, Larkfield, TX 00000
Icons may be used sparingly if they enhance clarity
The layout should feel organized and structured
Color and style
Use colors that complement the uploaded logo
Neutral, professional tones preferred
Avoid loud or saturated colors
The design should print well on standard cardstock
Print considerations
Design should be print‑ready
No edge to edge elements that risk being cut off
Proper margins and bleed awareness
Overall, the goal is a polished, high end business card that reflects trust, expertise, and professionalism consistent with a firm providing tax strategy, compliance, and advisory services.

```html
<!DOCTYPE html>
<html lang="en">
<head>
<meta charset="utf-8">
<title>Meridale Tax Advisers — Business Card</title>
<link rel="stylesheet" href="https://fonts.googleapis.com/css2?family=Montserrat:wght@400;600;700&family=Roboto:wght@400&display=swap">
<style>
  :root {
    --navy: #222456;
    --orange: #f26b1d;
    --white: #ffffff;
    --backdrop: #bdbdbd;
    --ink: #222456;
  }
  * { margin: 0; padding: 0; box-sizing: border-box; }
  html, body { width: 1200px; height: 1015px; overflow: hidden; }
  body {
    background: var(--backdrop);
    font-family: "Roboto", Arial, sans-serif;
    position: relative;
  }
  .card {
    position: absolute;
    left: 250px;
    width: 700px;
    height: 400px;
    box-shadow: 0 10px 24px rgba(0,0,0,0.35);
    overflow: hidden;
  }
  /* Front side */
  .card-front { top: 70px; background: var(--navy); color: var(--white); }
  .wordmark {
    position: absolute;
    font-family: "Montserrat", Arial, sans-serif;
    font-weight: 600;
    line-height: 1;
    display: flex;
    align-items: center;
    gap: 16px;
  }
  .wordmark-dot { width: 14px; height: 14px; border-radius: 50%; background: var(--orange); flex: none; }
  .wordmark-name { font-size: 46px; letter-spacing: 7px; text-transform: uppercase; }
  .wordmark-sub { display: block; font-size: 20px; letter-spacing: 9px; margin-top: 10px; }
  .card-front .wordmark { left: 50%; top: 142px; transform: translateX(-50%); color: var(--white); }
  .front-url {
    position: absolute; left: 0; right: 0; bottom: 40px;
    text-align: center; font-size: 15px; letter-spacing: 0.5px;
  }
  .front-rule {
    position: absolute; left: 50%; bottom: 0; transform: translateX(-50%);
    width: 190px; height: 6px; background: var(--orange);
  }
  /* Back side */
  .card-back { top: 545px; background: var(--white); color: var(--ink); }
  .card-back .wordmark { left: 48px; top: 70px; color: var(--navy); gap: 12px; }
  .card-back .wordmark-name { font-size: 34px; letter-spacing: 5px; }
  .card-back .wordmark-sub { font-size: 15px; letter-spacing: 7px; margin-top: 8px; }
  .corner-tab { position: absolute; right: 0; top: 40px; width: 14px; height: 36px; background: var(--navy); }
  .person { position: absolute; right: 36px; top: 38px; text-align: right; }
  .person-name { font-family: "Montserrat", Arial, sans-serif; font-weight: 700; font-size: 22px; color: var(--navy); }
  .person-creds { font-size: 11px; font-weight: 400; font-family: "Roboto", Arial, sans-serif; }
  .person-title { font-size: 16px; color: var(--orange); margin-top: 3px; }
  .address { position: absolute; left: 74px; top: 218px; font-size: 16px; line-height: 1.3; }
  .contacts { position: absolute; left: 74px; top: 275px; list-style: none; font-size: 16px; line-height: 21px; }
  .contacts li { display: flex; align-items: center; gap: 10px; }
  .contacts svg { width: 13px; height: 13px; flex: none; }
  .accent { color: var(--orange); }
</style>
</head>
<body>
  <section class="card card-front" aria-label="Card front">
    <div class="wordmark">
      <span class="wordmark-dot"></span>
      <span><span class="wordmark-name">Meridale</span><span class="wordmark-sub">Tax Advisers</span></span>
    </div>
    <p class="front-url">www.meridale.example</p>
    <div class="front-rule"></div>
  </section>

  <section class="card card-back" aria-label="Card back">
    <div class="corner-tab"></div>
    <div class="person">
      <p class="person-name">Peter L. Garnick<span class="person-creds">, MSA, CFP®, AIF®, EA</span></p>
      <p class="person-title">Managing Director, Tax</p>
    </div>
    <div class="wordmark">
      <span class="wordmark-dot"></span>
      <span><span class="wordmark-name">Meridale</span><span class="wordmark-sub">Tax Advisers</span></span>
    </div>
    <p class="address">2870 Fenwick Rd., Suite 415<br>Larkfield, TX 00000</p>
    <ul class="contacts">
      <li><svg viewBox="0 0 16 16" aria-hidden="true"><rect x="4" y="1" width="8" height="14" rx="1.5" fill="none" stroke="#f26b1d" stroke-width="1.8"/></svg><span>(555) 318-2047</span></li>
      <li><svg viewBox="0 0 16 16" aria-hidden="true"><path d="M3 2l3 0 1 3-2 1.5a8 8 0 0 0 4.5 4.5L11 9l3 1 0 3c0 1-1 1.5-2 1.5A11 11 0 0 1 1.5 4C1.5 3 2 2 3 2z" fill="#f26b1d"/></svg><span>(555) 642-7130 (Direct)</span></li>
      <li><svg viewBox="0 0 16 16" aria-hidden="true"><path d="M3 2l3 0 1 3-2 1.5a8 8 0 0 0 4.5 4.5L11 9l3 1 0 3c0 1-1 1.5-2 1.5A11 11 0 0 1 1.5 4C1.5 3 2 2 3 2z" fill="#f26b1d"/></svg><span>(555) 642-7188</span></li>
      <li><svg viewBox="0 0 16 16" aria-hidden="true"><rect x="1" y="3" width="14" height="10" fill="#f26b1d"/><path d="M1 3l7 6 7-6" fill="none" stroke="#fff" stroke-width="1.3"/></svg><span>pgarnick@mymeridale.example</span></li>
      <li><svg viewBox="0 0 16 16" aria-hidden="true"><circle cx="8" cy="8" r="6.5" fill="none" stroke="#f26b1d" stroke-width="1.6"/><ellipse cx="8" cy="8" rx="2.8" ry="6.5" fill="none" stroke="#f26b1d" stroke-width="1.2"/><path d="M1.5 8h13M3 4.5h10M3 11.5h10" stroke="#f26b1d" stroke-width="1.2"/></svg><span>www.<span class="accent">meridale</span>.example</span></li>
    </ul>
  </section>
</body>
</html>
```